Professional business card for the wholesale of metals, chemicals and waste

We are an established company in the wholesale trade of metals, chemicals and waste and are looking for a creative, professional design for our business card. The business card should reflect the values of our company - competence, reliability and innovative strength. It should convey both industry expertise and a modern, trustworthy image.
Important information for the design:

Logo: Our company logo must be prominently placed on the business card.
Colors: Please refer to the colors used on our website www.okr-gmbh.at. These colors should appear in the design to maintain the visual identity of our company.

QR Code: The business card should contain a QR code that contains all the information listed on the business card.
Font: Choose clear, easy-to-read fonts that reflect a modern, professional look.
Layout: The design should be clear and structured so that both text and visual elements (logo, QR code) are in a balanced relationship to each other.

Information that should appear on the business card:

Company name: OKR Handelsagenturen GmbH
Title: Dipl.-Ing.
Name: Lukas Fenwald
Position: Managing Director of Operations & Corporate Development
Phone: +43 4186 5921 48
Mobile: +43 664 58 37 216
Email: lukas.fenwald@okr-gmbh.at
Homepage: www.okr-gmbh.at

Design style:

Industry: Industrial yet modern style that conveys competence and trust.
Message: The business card should present our company as a leading supplier in the wholesale trade of metals, chemicals and waste – reliable, professional and innovative.
Target group: Our target group consists of B2B customers and industry contacts who are looking for high-quality products and services in the areas of metal trading, chemicals and waste management.

We look forward to creative designs that reflect our professional identity and are also modern and appealing. Your design should make a statement for our company!

```html
<!DOCTYPE html>
<html lang="en">
<head>
<meta charset="utf-8">
<title>OKR Handelsagenturen GmbH – Business Card</title>
<link rel="stylesheet" href="https://fonts.googleapis.com/css2?family=Poppins:wght@400;500;600;700&display=swap">
<style>
  :root {
    --navy: #1c2046;
    --white: #ffffff;
    --ink: #1a1a22;
    --stage: #232323;
  }
  * { box-sizing: border-box; margin: 0; padding: 0; }
  html, body {
    width: 1200px; height: 780px; overflow: hidden;
    background: var(--stage);
    font-family: "Poppins", Arial, sans-serif;
  }
  .sheet {
    width: 1200px; height: 780px;
    display: flex; align-items: center; justify-content: center; gap: 40px;
  }
  .card {
    position: relative;
    width: 540px; height: 310px;
    border-radius: 18px;
    overflow: hidden;
  }
  /* Front */
  .card--front { background: var(--white); color: var(--navy); }
  .edge-band {
    position: absolute; width: 10px; background: var(--navy);
  }
  .edge-band--left { left: 0; top: 46px; height: 112px; }
  .edge-band--right { right: 0; top: 150px; height: 112px; }
  .brand-mark {
    position: absolute; left: 38px; top: 58px;
    font-size: 66px; font-weight: 700; letter-spacing: 1px;
    color: var(--navy); line-height: 1;
  }
  .company-name {
    position: absolute; left: 28px; top: 236px;
    font-size: 12.5px; font-weight: 400; color: var(--navy);
  }
  .divider {
    position: absolute; left: 222px; top: 92px;
    width: 1px; height: 178px; background: var(--navy);
  }
  .person {
    position: absolute; left: 244px; top: 80px; right: 24px;
  }
  .person__name {
    font-size: 25px; line-height: 1.1; color: var(--navy); font-weight: 400;
  }
  .person__name strong { font-weight: 700; }
  .person__role {
    margin-top: 6px; font-size: 11.5px; line-height: 1.35; color: var(--ink);
  }
  .contact-list {
    list-style: none; margin-top: 12px;
    font-size: 11.5px; line-height: 1.55; color: var(--ink);
  }
  .contact-list li { display: flex; align-items: center; gap: 8px; }
  .contact-list svg { width: 11px; height: 11px; fill: var(--navy); flex: none; }
  /* Back */
  .card--back {
    background: var(--navy);
    display: flex; align-items: center; justify-content: center;
  }
  .card--back .brand-mark {
    position: static; color: var(--white); font-size: 96px;
  }
</style>
</head>
<body>
<main class="sheet">
  <section class="card card--front" aria-label="Business card front">
    <span class="edge-band edge-band--left"></span>
    <span class="edge-band edge-band--right"></span>
    <div class="brand-mark">OKR</div>
    <p class="company-name">OKR Handelsagenturen GmbH</p>
    <span class="divider"></span>
    <div class="person">
      <h1 class="person__name"><strong>Lukas</strong> Fenwald</h1>
      <p class="person__role">Dipl.-Ing.<br>Managing Director of Operations<br>&amp; Corporate Development</p>
      <ul class="contact-list">
        <li>
          <svg viewBox="0 0 24 24" aria-hidden="true"><path d="M6.6 10.8a15 15 0 0 0 6.6 6.6l2.2-2.2a1 1 0 0 1 1-.25 11.4 11.4 0 0 0 3.6.57 1 1 0 0 1 1 1V20a1 1 0 0 1-1 1A17 17 0 0 1 3 4a1 1 0 0 1 1-1h3.5a1 1 0 0 1 1 1c0 1.25.2 2.45.57 3.6a1 1 0 0 1-.25 1z"/></svg>
          +43 4186 5921 48
        </li>
        <li>
          <svg viewBox="0 0 24 24" aria-hidden="true"><path d="M7 1h10a2 2 0 0 1 2 2v18a2 2 0 0 1-2 2H7a2 2 0 0 1-2-2V3a2 2 0 0 1 2-2zm0 3v14h10V4zm5 15.5a1.2 1.2 0 1 0 0 2.4 1.2 1.2 0 0 0 0-2.4z"/></svg>
          +43 664 58 37 216
        </li>
        <li>
          <svg viewBox="0 0 24 24" aria-hidden="true"><path d="M12 2a10 10 0 1 0 0 20 10 10 0 0 0 0-20zm6.9 9h-3a15.6 15.6 0 0 0-1.3-5.6A8 8 0 0 1 18.9 11zM12 4.1c.9 1.2 1.8 3.6 2 6.9h-4c.2-3.3 1.1-5.7 2-6.9zM9.4 5.4A15.6 15.6 0 0 0 8.1 11h-3a8 8 0 0 1 4.3-5.6zM5.1 13h3a15.6 15.6 0 0 0 1.3 5.6A8 8 0 0 1 5.1 13zm6.9 6.9c-.9-1.2-1.8-3.6-2-6.9h4c-.2 3.3-1.1 5.7-2 6.9zm2.6-1.3a15.6 15.6 0 0 0 1.3-5.6h3a8 8 0 0 1-4.3 5.6z"/></svg>
          www.okr-gmbh.at
        </li>
        <li>
          <svg viewBox="0 0 24 24" aria-hidden="true"><path d="M3 5h18a1 1 0 0 1 1 1v12a1 1 0 0 1-1 1H3a1 1 0 0 1-1-1V6a1 1 0 0 1 1-1zm1 2.3V17h16V7.3l-8 5.2z M5.5 7 12 11.2 18.5 7z"/></svg>
          lukas.fenwald@okr-gmbh.at
        </li>
      </ul>
    </div>
  </section>

  <section class="card card--back" aria-label="Business card back">
    <div class="brand-mark">OKR</div>
  </section>
</main>
</body>
</html>
```